Stationery Design Project - KLVA Partners

Business Cards
Size: 90mm x 55mm
Letterhead
Size: A4 - 210mm x 297mm
With Compliments Slip
Size: DL - 210mm x 99mm
Presentation Folder
Size: A4

KLVA Partners
website: www.klvapartners.com.au (Under construction)
Offices: *Perth *Brisbane * Seoul

A company that supply Safety consultantcy services

Industry/Entity Type

Business

```html
<!DOCTYPE html>
<html lang="en">
<head>
<meta charset="utf-8">
<title>KLVA Partners — Stationery</title>
<link href="https://fonts.googleapis.com/css2?family=Noto+Sans:wght@300;400&display=swap" rel="stylesheet">
<style>
  :root{
    --bg:#d9d9d9;
    --paper:#ffffff;
    --ink:#222222;
    --muted:#8a8a8a;
    --brand-grey:#5e5e5e;
    --blue-dark:#1d3f7a;
    --blue:#2a62a6;
    --blue-light:#4b97d2;
    --accent:#3f86c8;
    --wedge:#9a9a9a;
  }
  *{box-sizing:border-box;margin:0;padding:0}
  html,body{width:1200px;height:900px;overflow:hidden}
  body{background:var(--bg);font-family:"Noto Sans",Verdana,sans-serif;color:var(--ink);position:relative}
  .sheet{position:absolute;background:var(--paper);overflow:hidden}
  .brand{position:absolute;display:flex;align-items:center;gap:10px}
  .brand-mark{background:var(--blue);display:block}
  .brand-name{font-weight:300;color:var(--brand-grey);letter-spacing:.5px;white-space:nowrap}
  .contact{position:absolute;list-style:none;font-size:8.5px;color:var(--muted);line-height:10.5px}
  .contact li{display:flex;gap:6px}
  .contact svg{width:8px;height:8px;flex:none;margin-top:1px;fill:var(--muted)}
  .contact .indent{padding-left:14px}
  .band{position:absolute;left:0;width:100%}
  .band svg{position:absolute;inset:0;width:100%;height:100%}
  .band-label{position:absolute;color:#fff;white-space:nowrap}
  .offices{color:var(--accent)}

  /* letterhead */
  .letterhead{left:123px;top:50px;width:566px;height:800px}
  .letterhead .brand{left:47px;top:65px}
  .letterhead .brand-mark{width:50px;height:50px}
  .letterhead .brand-name{font-size:28px}
  .letterhead .contact{left:410px;top:57px}
  .recipient{position:absolute;left:63px;top:183px;font-size:10.5px;line-height:15px}
  .salutation{position:absolute;left:63px;top:243px;font-size:10.5px}
  .letter-body{position:absolute;left:63px;top:273px;width:447px;font-size:10px;line-height:15px;text-align:justify}
  .letter-body p{margin-bottom:15px}
  .signature{position:absolute;left:60px;top:585px;width:162px;height:38px;background:linear-gradient(90deg,#e4e8f3,#f4f6fb)}
  .signoff{position:absolute;left:63px;top:624px;font-size:10.5px;line-height:15px}
  .letterhead .band{top:708px;height:92px}
  .letterhead .band-label{left:220px;top:66px;font-size:10.5px}

  /* compliments slip */
  .slip{left:513px;top:193px;width:565px;height:267px}
  .slip .brand{left:36px;top:38px}
  .slip .brand-mark{width:50px;height:50px}
  .slip .brand-name{font-size:26px}
  .slip .offices{position:absolute;left:430px;top:21px;font-size:10px}
  .slip .contact{left:430px;top:40px}
  .slip .band{top:178px;height:89px}
  .slip .band-label{left:220px;top:59px;font-size:12.5px;letter-spacing:.3px}

  /* business cards */
  .card{left:757px;width:243px;height:148px}
  .card-front{top:508px}
  .card-front .brand{left:22px;top:30px;gap:7px}
  .card-front .brand-mark{width:36px;height:36px}
  .card-front .brand-name{font-size:19px}
  .card-front .band{top:88px;height:60px}
  .card-front .band-label{left:72px;top:35px;font-size:8px}
  .card-back{top:676px}
  .card-back .band{top:0;height:64px}
  .holder{position:absolute;left:23px;top:74px;color:var(--accent)}
  .holder-name{font-size:11px;letter-spacing:.3px}
  .holder-title{font-size:7.5px}
  .card-back .contact{left:115px;top:75px;font-size:7.5px;line-height:9.8px}
  .card-back .contact svg{width:7px;height:7px}
</style>
</head>
<body>

<svg width="0" height="0" style="position:absolute" aria-hidden="true">
  <defs>
    <symbol id="icon-pin" viewBox="0 0 10 10"><path d="M5 0a3.4 3.4 0 0 0-3.4 3.4C1.6 6 5 10 5 10s3.4-4 3.4-6.6A3.4 3.4 0 0 0 5 0zm0 4.8a1.4 1.4 0 1 1 0-2.8 1.4 1.4 0 0 1 0 2.8z"/></symbol>
    <symbol id="icon-web" viewBox="0 0 10 10"><path d="M5 0a5 5 0 1 0 0 10A5 5 0 0 0 5 0zm0 1a4 4 0 0 1 3.9 3.5H1.1A4 4 0 0 1 5 1zM1.1 5.5h7.8A4 4 0 0 1 5 9a4 4 0 0 1-3.9-3.5z"/></symbol>
    <symbol id="icon-phone" viewBox="0 0 10 10"><path d="M2 0l2 2.4-1.1 1.2a6 6 0 0 0 3.5 3.5L7.6 6 10 8 8.6 9.6C4.6 10 0 5.4.4 1.4z"/></symbol>
    <symbol id="icon-mobile" viewBox="0 0 10 10"><path d="M3 0h4a1 1 0 0 1 1 1v8a1 1 0 0 1-1 1H3a1 1 0 0 1-1-1V1a1 1 0 0 1 1-1zm0 1.5v6h4v-6z"/></symbol>
    <symbol id="icon-fax" viewBox="0 0 10 10"><path d="M2.5 0h5v3h-5zM0 3.5h10V8H8v2H2V8H0zm3 3.5v2h4V7z"/></symbol>
    <linearGradient id="band-blue" x1="0" x2="1" y1="0" y2="0">
      <stop offset="0" stop-color="#1d3f7a"/>
      <stop offset=".55" stop-color="#24569a"/>
      <stop offset="1" stop-color="#4b97d2"/>
    </linearGradient>
    <linearGradient id="band-wedge" x1="0" x2="1" y1="0" y2="0">
      <stop offset="0" stop-color="#8c8c8c"/>
      <stop offset="1" stop-color="#d0d0d0"/>
    </linearGradient>
  </defs>
</svg>

<!-- Letterhead -->
<section class="sheet letterhead" aria-label="Letterhead">
  <div class="brand"><span class="brand-mark"></span><span class="brand-name">KLVA Partners</span></div>
  <ul class="contact">
    <li><svg><use href="#icon-pin"/></svg>42 Harbour Lane Claremont,</li>
    <li class="indent">Western Australia</li>
    <li><svg><use href="#icon-web"/></svg>www.klvapartners.com.au</li>
    <li><svg><use href="#icon-phone"/></svg>08 5550 0142</li>
    <li><svg><use href="#icon-fax"/></svg>08 5550 0187</li>
  </ul>
  <address class="recipient" style="font-style:normal">Laura Benton<br>18 Maple Ave<br>Greenfield MA</address>
  <p class="salutation">Dear Mrs Laura Benton,</p>
  <div class="letter-body">
    <p>Lorem ipsum dolor sit amet, consectetur adipiscing elit. Integer aliquet consectetur et id orci. Praesent vitae felis vitae justo elementum turpis semper dui elementum nec aliquet lectus pulvinar. Donec congue congue risus congue a. Maecenas commodo, nisi a gravida condimentum leo, in pellentesque elit erat id nisi. Pellentesque commodo. Nam tincidunt viverra elit at hendrerit. Quisque eget purus tellus. Maecenas pulvinar consectetur.</p>
    <p>Nunc molestie iaculis orci, vitae consequat mi condimentum vitae. Etiam magna tellus. Proin quam augue, vehicula sed euismod in, vehicula eu felis. Pellentesque a orci ac turpis commodo varius at ut arcu. Integer viverra semper sapien fermentum egestas. Curabitur erat purus, congue et faucibus sit amet, fringilla elementum odio. Sed pretium tincidunt mi, nec fermentum urna interdum sed. Nam et lectus turpis, quis cursus ipsum. Maecenas non nibh odio. Sed in laoreet justo.</p>
    <p>Aenean sed sem lacus. Vivamus auctor, sapien non aliquet ultrices, mauris turpis porttitor nisl, id rutrum velit erat non urna. Praesent eu augue eu ligula feugiat malesuada. Proin nec nibh erat. Sed et leo id leo volutpat viverra non ac mi. In quis dictum magna. Donec ut dui sed dui tristique dictum. Donec varius sapien sed turpis dictum a dignissim diam facilisis.</p>
  </div>
  <div class="signature" role="img" aria-label="Handwritten signature"></div>
  <p class="signoff">Yours Sincerely<br>Daniel Archer</p>
  <div class="band">
    <svg viewBox="0 0 566 92" preserveAspectRatio="none" aria-hidden="true">
      <polygon points="0,0 255,34 0,24" fill="url(#band-wedge)"/>
      <polygon points="0,24 255,34 566,10 566,92 0,92" fill="url(#band-blue)"/>
    </svg>
    <span class="band-label">Perth &bull; Brisbane &bull; Seoul</span>
  </div>
</section>

<!-- With compliments slip -->
<section class="sheet slip" aria-label="With compliments slip">
  <div class="brand"><span class="brand-mark"></span><span class="brand-name">KLVA Partners</span></div>
  <p class="offices">Perth &bull; Brisbane &bull; Seoul</p>
  <ul class="contact">
    <li><svg><use href="#icon-pin"/></svg>42 Harbour Lane Claremont,</li>
    <li class="indent">Western Australia</li>
    <li><svg><use href="#icon-web"/></svg>www.klvapartners.com.au</li>
    <li><svg><use href="#icon-phone"/></svg>08 5550 0142</li>
    <li><svg><use href="#icon-fax"/></svg>08 5550 0187</li>
  </ul>
  <div class="band">
    <svg viewBox="0 0 565 89" preserveAspectRatio="none" aria-hidden="true">
      <polygon points="0,0 255,34 0,22" fill="url(#band-wedge)"/>
      <polygon points="0,22 255,34 565,12 565,89 0,89" fill="url(#band-blue)"/>
    </svg>
    <span class="band-label">WITH COMPLIMENTS</span>
  </div>
</section>

<!-- Business card, front -->
<section class="sheet card card-front" aria-label="Business card front">
  <div class="brand"><span class="brand-mark"></span><span class="brand-name">KLVA Partners</span></div>
  <div class="band">
    <svg viewBox="0 0 243 60" preserveAspectRatio="none" aria-hidden="true">
      <polygon points="0,0 110,16 0,10" fill="url(#band-wedge)"/>
      <polygon points="0,10 110,16 243,5 243,60 0,60" fill="url(#band-blue)"/>
    </svg>
    <span class="band-label">Perth &bull; Brisbane &bull; Seoul</span>
  </div>
</section>

<!-- Business card, back -->
<section class="sheet card card-back" aria-label="Business card back">
  <div class="band">
    <svg viewBox="0 0 243 64" preserveAspectRatio="none" aria-hidden="true">
      <polygon points="0,0 243,0 243,36 110,48 0,34" fill="url(#band-blue)"/>
      <polygon points="0,34 110,48 0,46" fill="url(#band-wedge)"/>
    </svg>
  </div>
  <div class="holder">
    <p class="holder-name">DANIEL ARCHER</p>
    <p class="holder-title">Australian Director</p>
  </div>
  <ul class="contact">
    <li><svg><use href="#icon-pin"/></svg>42 Harbour Lane Claremont,</li>
    <li class="indent">Western Australia</li>
    <li><svg><use href="#icon-web"/></svg>www.klvapartners.com.au</li>
    <li><svg><use href="#icon-phone"/></svg>08 5550 0142</li>
    <li><svg><use href="#icon-mobile"/></svg>0400 555 318</li>
    <li><svg><use href="#icon-fax"/></svg>08 5550 0187</li>
  </ul>
</section>

</body>
</html>
```